TALBRIDGE ELEVATOR CORP

LOOKING FOR BLACK MATTE BACKGROUND WITH GLOSS DESIGN
NEED RAISED UV ON LOGO AND LETTERING , WITH ROUNDED CORNERS AND COLORED EDGES ( FLOURECENT BLUE)

```html
<!DOCTYPE html>
<html lang="en">
<head>
<meta charset="utf-8">
<title>Talbridge Elevator Corp — Business Card</title>
<link rel="stylesheet" href="https://fonts.googleapis.com/css2?family=Roboto:wght@400;500&family=Tinos:wght@400&display=swap">
<style>
  :root {
    --scene-bg: #e6e6e4;
    --card-black: #2b2b2c;
    --edge-blue: #3a86d8;
    --accent-blue: #3d8ee0;
    --text-light: #ecedee;
    --text-muted: #cfd1d3;
    --gloss-dark: #3b3b3d;
    --gloss-light: #9a9a9c;
    --logo-circle: #2f7fc9;
  }
  * { box-sizing: border-box; margin: 0; padding: 0; }
  html, body { width: 1200px; height: 801px; overflow: hidden; }
  body {
    background: var(--scene-bg);
    font-family: "Roboto", Arial, sans-serif;
    position: relative;
  }
  .card {
    position: absolute;
    width: 500px;
    height: 286px;
    background: var(--card-black);
    border-radius: 12px;
    border-right: 3px solid var(--edge-blue);
    border-bottom: 3px solid var(--edge-blue);
    overflow: hidden;
  }
  .card--front { left: 70px; top: 258px; }
  .card--back { left: 630px; top: 258px; }

  /* Front */
  .brand {
    position: absolute;
    right: 34px;
    top: 36px;
    display: flex;
    align-items: center;
    gap: 14px;
  }
  .brand__mark {
    width: 62px; height: 62px; border-radius: 50%;
    background: var(--logo-circle);
  }
  .brand__text { font-family: "Tinos", "Times New Roman", serif; color: var(--text-light); }
  .brand__name { font-size: 19px; letter-spacing: 0.5px; }
  .brand__rule { height: 1px; background: var(--text-light); margin: 4px 0 3px; }
  .brand__tag { font-size: 12px; letter-spacing: 1px; text-align: right; }

  .address {
    position: absolute;
    right: 34px; top: 118px;
    text-align: right;
    color: var(--text-light);
    font-size: 13px;
    line-height: 1.45;
  }
  .divider {
    position: absolute;
    left: 34px; right: 34px; top: 162px;
    height: 1px; background: var(--text-muted);
  }
  .person {
    position: absolute; left: 34px; top: 172px;
  }
  .person__name { color: var(--accent-blue); font-size: 19px; font-weight: 500; }
  .person__title { color: var(--text-light); font-size: 13px; margin-top: 1px; }
  .contacts {
    position: absolute; left: 34px; top: 218px;
    list-style: none;
    color: var(--text-light);
    font-size: 12.5px;
    line-height: 1.55;
  }
  .contacts li { display: flex; align-items: center; gap: 8px; }
  .contacts svg { width: 11px; height: 11px; fill: none; stroke: var(--accent-blue); stroke-width: 1.6; }
  .contacts .web-host { color: var(--accent-blue); }

  /* Back */
  .emboss {
    position: absolute; left: 0; right: 0; top: 36px;
    display: flex; flex-direction: column; align-items: center;
  }
  .emboss__mark {
    width: 120px; height: 120px; border-radius: 50%;
    background: radial-gradient(circle at 40% 30%, var(--gloss-light), var(--gloss-dark) 70%);
  }
  .emboss__name {
    margin-top: 14px;
    font-family: "Tinos", "Times New Roman", serif;
    font-size: 29px; letter-spacing: 0.5px;
    color: var(--gloss-light);
  }
  .emboss__tagline {
    display: flex; align-items: center; gap: 10px; width: 430px; margin-top: 2px;
    font-family: "Tinos", "Times New Roman", serif;
    font-size: 17px; letter-spacing: 1px; color: var(--gloss-light);
  }
  .emboss__tagline::before, .emboss__tagline::after {
    content: ""; flex: 1; height: 2px; background: var(--gloss-light);
  }
</style>
</head>
<body>
  <section class="card card--front" aria-label="Card front">
    <div class="brand">
      <div class="brand__mark"></div>
      <div class="brand__text">
        <div class="brand__name">TALBRIDGE ELEVATOR CORP</div>
        <div class="brand__rule"></div>
        <div class="brand__tag">ELEVATOR SERVICES</div>
      </div>
    </div>
    <address class="address" style="font-style:normal">
      2210 Harlan Avenue<br>Bronx, Ny 10460
    </address>
    <div class="divider"></div>
    <div class="person">
      <div class="person__name">Daniel Hartwell</div>
      <div class="person__title">President</div>
    </div>
    <ul class="contacts">
      <li><svg viewBox="0 0 12 12"><path d="M3 1.5l2 2-1.2 1.4a6 6 0 0 0 3.3 3.3L8.5 7l2 2-1.5 1.5C5 10 2 7 1.5 3z"/></svg>555-014-2278</li>
      <li><svg viewBox="0 0 12 12"><rect x="1" y="2.5" width="10" height="7"/><path d="M1 2.5l5 4 5-4"/></svg>talbridgeelevator@mail.com</li>
      <li><svg viewBox="0 0 12 12"><circle cx="6" cy="6" r="5"/><path d="M1 6h10M6 1c2.5 3 2.5 7 0 10M6 1c-2.5 3-2.5 7 0 10"/></svg>www.<span class="web-host">talbridgeelevatorny</span>.com</li>
    </ul>
  </section>

  <section class="card card--back" aria-label="Card back">
    <div class="emboss">
      <div class="emboss__mark"></div>
      <div class="emboss__name">TALBRIDGE ELEVATOR CORP</div>
      <div class="emboss__tagline">ELEVATOR SERVICES</div>
    </div>
  </section>
</body>
</html>
```